Mesh Banner Design for Business Premises

We require the design of a large mesh banner to be installed across the front fence of our warehouse. The banner should prominently feature our existing Trelborn logo and brand colours (yellow, white, and black) and be designed to be highly visible from the road.

The overall aesthetic should be strong, masculine, and industrial, reflecting the nature of the scaffolding and construction industry. The background should be predominantly black, with our branding incorporated in yellow and white for strong contrast and readability.

The banner should clearly communicate the full scope of services we provide, including:

Scaffold Design
Scaffold Engineering
Scaffold Installation / Erection
Scaffold Dismantling

It should also indicate the types of projects and clients we service, including:

Commercial
Industrial
Residential
Civil

The design should feel bold and professional, with a construction-oriented style that aligns with the scaffolding industry. It should be clean, impactful, and easy to read from a distance, ensuring passing traffic can quickly understand our services.

Where possible, subtle industrial or structural design elements (such as scaffold components, steel textures, or linework) may be incorporated into the background to reinforce the industry theme while keeping the layout uncluttered.

The final design will be produced as a large-format mesh banner for outdoor installation, so it should be created with this application and viewing distance in mind.

```html
<!DOCTYPE html>
<html lang="en">
<head>
<meta charset="utf-8">
<title>Trelborn Mesh Banner</title>
<link href="https://fonts.googleapis.com/css2?family=Montserrat:ital,wght@0,400;0,600;0,700;1,700&family=Oswald:wght@600&display=swap" rel="stylesheet">
<style>
:root{
  --yellow:#f5a91c;
  --ink:#0b0d12;
  --navy:#1a2740;
  --steel:#2c3f63;
  --white:#ffffff;
  --page:#ffffff;
}
*{box-sizing:border-box;margin:0;padding:0}
html,body{width:992px;height:1200px;overflow:hidden;background:var(--page)}
body{position:relative;font-family:"Montserrat",sans-serif}
.banner{
  position:absolute;left:20px;top:362px;width:952px;height:476px;
  background:var(--ink);overflow:hidden;
  box-shadow:0 8px 24px rgba(0,0,0,.25);
}
.backdrop{
  position:absolute;inset:0;
  background:
    radial-gradient(ellipse at 30% 45%, rgba(44,63,99,.75), rgba(11,13,18,0) 60%),
    linear-gradient(135deg, var(--navy) 0%, #121a2b 45%, var(--ink) 80%);
}
.brand{position:absolute;left:44px;top:60px;display:flex;align-items:center;gap:14px}
.brand-mark{width:40px;height:40px;background:var(--yellow)}
.brand-name{
  color:var(--white);font-weight:600;font-size:26px;letter-spacing:11px;
}
.tagline{
  position:absolute;left:518px;top:61px;width:434px;height:37px;
  background:var(--yellow);clip-path:polygon(12px 0,100% 0,100% 100%,0 100%);
  color:var(--ink);font-style:italic;font-weight:700;font-size:19px;
  display:flex;align-items:center;padding-left:26px;
}
.headline{
  position:absolute;left:42px;top:172px;
  font-family:"Oswald",sans-serif;font-weight:600;font-size:44px;line-height:52px;
  color:var(--white);text-transform:uppercase;
}
.headline .accent{color:var(--yellow)}
.services-label{
  position:absolute;left:376px;top:185px;width:177px;height:28px;
  background:var(--white);clip-path:polygon(10px 0,100% 0,calc(100% - 10px) 100%,0 100%);
  color:var(--ink);font-weight:700;font-size:17px;
  display:flex;align-items:center;padding-left:17px;
}
.service{
  position:absolute;display:flex;align-items:center;gap:8px;
  color:var(--white);font-weight:600;font-size:15px;white-space:nowrap;
}
.service svg{width:20px;height:20px;flex:none}
.sectors{position:absolute;left:0;top:347px;width:100%;height:52px}
.sector{
  position:absolute;top:0;height:52px;transform:translateX(-50%);
  display:flex;align-items:center;justify-content:center;text-align:center;
  color:var(--white);font-weight:700;font-size:15px;line-height:19px;white-space:nowrap;
}
.sector-divider{position:absolute;top:0;width:1px;height:52px;background:var(--yellow)}
.footer-strip{position:absolute;left:0;top:427px;width:100%;height:49px}
.coverage{
  position:absolute;left:0;top:0;width:545px;height:49px;background:var(--white);
  clip-path:polygon(0 0,100% 0,calc(100% - 24px) 100%,0 100%);
  display:flex;align-items:center;padding-left:37px;
  color:var(--ink);font-size:17px;font-weight:400;
}
.coverage strong{font-weight:700;margin-left:5px}
.contact{
  position:absolute;left:520px;top:0;right:0;height:49px;background:var(--yellow);
  clip-path:polygon(24px 0,100% 0,100% 100%,0 100%);
  color:var(--ink);font-weight:700;font-size:18px;
}
.contact .phone{position:absolute;left:38px;top:0;line-height:49px}
.contact .divider{position:absolute;left:185px;top:8px;width:1px;height:33px;background:var(--ink)}
.contact .web{position:absolute;left:201px;top:0;line-height:49px}
</style>
</head>
<body>
<section class="banner">
  <div class="backdrop" role="img" aria-label="Dark photograph of scaffolding tubes silhouetted against a blue sky"></div>

  <div class="brand">
    <span class="brand-mark"></span>
    <span class="brand-name">TRELBORN</span>
  </div>

  <div class="tagline">Safe, Superior Scaffolding Solutions</div>

  <h1 class="headline"><span class="accent">Strength</span> You<br>Can Rely On</h1>

  <div class="services-label">OUR SERVICES</div>

  <div class="service" style="left:376px;top:232px">
    <svg viewBox="0 0 20 20"><circle cx="10" cy="10" r="8.5" fill="none" stroke="#f5a91c" stroke-width="1.5"/><path d="M6 10.5l3 3 5-7" fill="none" stroke="#f5a91c" stroke-width="1.8" stroke-linecap="round" stroke-linejoin="round"/></svg>
    Design &amp; Engineering
  </div>
  <div class="service" style="left:376px;top:268px">
    <svg viewBox="0 0 20 20"><circle cx="10" cy="10" r="8.5" fill="none" stroke="#f5a91c" stroke-width="1.5"/><path d="M6 10.5l3 3 5-7" fill="none" stroke="#f5a91c" stroke-width="1.8" stroke-linecap="round" stroke-linejoin="round"/></svg>
    Steel &amp; Aluminium Systems
  </div>
  <div class="service" style="left:648px;top:196px">
    <svg viewBox="0 0 20 20"><circle cx="10" cy="10" r="8.5" fill="none" stroke="#f5a91c" stroke-width="1.5"/><path d="M6 10.5l3 3 5-7" fill="none" stroke="#f5a91c" stroke-width="1.8" stroke-linecap="round" stroke-linejoin="round"/></svg>
    Erection &amp; Dismantle
  </div>
  <div class="service" style="left:648px;top:232px">
    <svg viewBox="0 0 20 20"><circle cx="10" cy="10" r="8.5" fill="none" stroke="#f5a91c" stroke-width="1.5"/><path d="M6 10.5l3 3 5-7" fill="none" stroke="#f5a91c" stroke-width="1.8" stroke-linecap="round" stroke-linejoin="round"/></svg>
    Specialised Access Solutions
  </div>
  <div class="service" style="left:648px;top:268px">
    <svg viewBox="0 0 20 20"><circle cx="10" cy="10" r="8.5" fill="none" stroke="#f5a91c" stroke-width="1.5"/><path d="M6 10.5l3 3 5-7" fill="none" stroke="#f5a91c" stroke-width="1.8" stroke-linecap="round" stroke-linejoin="round"/></svg>
    Mobile Scaffold Hire
  </div>

  <div class="sectors">
    <div class="sector" style="left:210px">COMMERCIAL<br>&amp; RETAIL</div>
    <span class="sector-divider" style="left:297px"></span>
    <div class="sector" style="left:381px">INDUSTRIAL &amp;<br>GOVERNMENT</div>
    <span class="sector-divider" style="left:466px"></span>
    <div class="sector" style="left:551px">RESIDENTIAL<br>&amp; DOMESTIC</div>
    <span class="sector-divider" style="left:633px"></span>
    <div class="sector" style="left:738px">CIVIL &amp;<br>INFRASTRUCTURE</div>
  </div>

  <div class="footer-strip">
    <div class="coverage">Servicing<strong>Brisbane, Gold Coast &amp; Sunshine Coast</strong></div>
    <div class="contact">
      <span class="phone">1300 8 RISE</span>
      <span class="divider"></span>
      <span class="web">TRELBORN.COM.AU</span>
    </div>
  </div>
</section>
</body>
</html>
```